DOG DAYCARE BILLBOARD

Design a bold exciting billboard that can be read easily from a distance! Our goal is brand awareness and showcasing the services we offer (Boarding, Grooming, Daycare, and Training.
we would like to see examples with the phrase "your best friend's best day". Our name Bright Meadow Canine Activity Center (or just Bright Meadow might work better and could be bigger) and the services we provide.
(there are two examples of what we like included in the pictures)
you can find more information o our website at pawplayhub@mailnest.example.

```html
<!DOCTYPE html>
<html lang="en">
<head>
<meta charset="utf-8">
<title>Bright Meadow Billboard</title>
<link rel="stylesheet" href="https://fonts.googleapis.com/css2?family=Bebas+Neue&family=Fredoka:wght@600&family=Arimo:wght@700&display=swap">
<style>
  :root {
    --sky: #7ab3e0;
    --ink: #111418;
    --white: #ffffff;
    --photo-dark: #2c3140;
    --photo-warm: #8a7356;
    --pups-warm: #b89676;
    --pups-light: #e6ddd3;
    --ring: #d7d7d7;
  }
  * { margin: 0; padding: 0; box-sizing: border-box; }
  html, body { width: 1200px; height: 2400px; overflow: hidden; background: var(--white); }
  .canvas { position: relative; width: 1200px; height: 2400px; background: var(--white); }
  .billboard {
    position: absolute; left: 50px; top: 945px; width: 1100px; height: 511px;
    background: var(--sky); overflow: hidden;
    box-shadow: 0 2px 6px rgba(0,0,0,.25);
  }
  .hero-photo { position: absolute; inset: 0; width: 1100px; height: 511px; }
  .brand-name {
    position: absolute; left: 62px; top: 28px;
    font-family: "Bebas Neue", sans-serif; font-size: 122px; line-height: 1;
    color: var(--ink); letter-spacing: 1px; white-space: nowrap;
  }
  .tagline {
    position: absolute; left: 40px; width: 580px; top: 148px;
    font-family: "Fredoka", sans-serif; font-weight: 600; font-size: 54px;
    line-height: 60px; color: var(--white); text-align: center;
  }
  .services {
    position: absolute; left: 72px; top: 285px; width: 560px;
    display: grid; grid-template-columns: 316px 1fr; row-gap: 22px;
    list-style: none;
  }
  .service {
    display: flex; align-items: center; gap: 14px;
    font-family: "Arimo", sans-serif; font-weight: 700; font-size: 25px;
    color: var(--ink); line-height: 34px;
  }
  .paw { width: 36px; height: 34px; flex: none; }
  .contact-strip {
    position: absolute; left: 300px; top: 444px; width: 620px; height: 42px;
    background: var(--white);
  }
  .contact {
    position: absolute; left: 330px; top: 444px; height: 42px;
    display: flex; align-items: center; gap: 16px;
    font-family: "Arimo", sans-serif; font-weight: 700; font-size: 25px; color: var(--ink);
  }
  .mail-icon { width: 34px; height: 24px; }
  .pups-photo {
    position: absolute; left: 0; top: 391px; width: 306px; height: 120px;
    background: linear-gradient(90deg, var(--pups-light), var(--pups-warm) 40%, var(--pups-light) 70%, var(--pups-warm));
    border-top-right-radius: 60px 50px;
  }
  .brand-badge {
    position: absolute; left: 674px; top: 158px; width: 148px; height: 148px;
    border-radius: 50%; background: var(--white); border: 3px solid var(--ring);
    display: flex; align-items: center; justify-content: center; text-align: center;
    font-family: "Arimo", sans-serif; font-weight: 700; font-size: 20px; color: var(--ink);
    line-height: 1.1;
  }
</style>
</head>
<body>
<div class="canvas">
  <section class="billboard">
    <svg class="hero-photo" viewBox="0 0 1100 511" role="img" aria-label="Photo of a groomed Yorkshire terrier on a grooming table with a groomer holding a tool">
      <defs>
        <linearGradient id="heroTone" x1="0" y1="0" x2="1" y2="1">
          <stop offset="0" stop-color="#3a4154"/>
          <stop offset="0.45" stop-color="var(--photo-warm)"/>
          <stop offset="1" stop-color="var(--photo-dark)"/>
        </linearGradient>
      </defs>
      <circle cx="1100" cy="252" r="391" fill="url(#heroTone)" stroke="#ffffff" stroke-width="6"/>
    </svg>

    <h1 class="brand-name">BRIGHT MEADOW</h1>
    <p class="tagline">your Best Friend's<br>Best Day</p>

    <ul class="services">
      <li class="service"><svg class="paw" viewBox="0 0 36 34"><g fill="#fff"><ellipse cx="18" cy="24" rx="10" ry="8"/><ellipse cx="5" cy="14" rx="4" ry="5"/><ellipse cx="13" cy="6" rx="4" ry="5.5"/><ellipse cx="23" cy="6" rx="4" ry="5.5"/><ellipse cx="31" cy="14" rx="4" ry="5"/></g></svg>BOARDING</li>
      <li class="service"><svg class="paw" viewBox="0 0 36 34"><g fill="#fff"><ellipse cx="18" cy="24" rx="10" ry="8"/><ellipse cx="5" cy="14" rx="4" ry="5"/><ellipse cx="13" cy="6" rx="4" ry="5.5"/><ellipse cx="23" cy="6" rx="4" ry="5.5"/><ellipse cx="31" cy="14" rx="4" ry="5"/></g></svg>DAYCARE</li>
      <li class="service"><svg class="paw" viewBox="0 0 36 34"><g fill="#fff"><ellipse cx="18" cy="24" rx="10" ry="8"/><ellipse cx="5" cy="14" rx="4" ry="5"/><ellipse cx="13" cy="6" rx="4" ry="5.5"/><ellipse cx="23" cy="6" rx="4" ry="5.5"/><ellipse cx="31" cy="14" rx="4" ry="5"/></g></svg>GROOMING</li>
      <li class="service"><svg class="paw" viewBox="0 0 36 34"><g fill="#fff"><ellipse cx="18" cy="24" rx="10" ry="8"/><ellipse cx="5" cy="14" rx="4" ry="5"/><ellipse cx="13" cy="6" rx="4" ry="5.5"/><ellipse cx="23" cy="6" rx="4" ry="5.5"/><ellipse cx="31" cy="14" rx="4" ry="5"/></g></svg>TRAINING</li>
    </ul>

    <div class="contact-strip"></div>
    <p class="contact">
      <svg class="mail-icon" viewBox="0 0 34 24"><rect x="1.5" y="1.5" width="31" height="21" fill="none" stroke="#111418" stroke-width="2.5"/><path d="M1.5 1.5 L17 13 L32.5 1.5 M1.5 22.5 L13 10 M32.5 22.5 L21 10" fill="none" stroke="#111418" stroke-width="2.5"/></svg>
      pawplayhub@mailnest.example
    </p>

    <div class="pups-photo" role="img" aria-label="Photo of four puppies in a row: a terrier mix, a bulldog, a pug and a beagle"></div>

    <div class="brand-badge">Bright<br>Meadow</div>
  </section>
</div>
</body>
</html>
```